Specialty Contact lens for children

We need a large size canvas 24x36" to advertise specialty fit contact lens for children to control myopia. please visit our website for more about our office theme www.tarnobelle.com
We want modern , fresh, happy design. Color blue, green, white. Final design should communicate the best lens choice for the children. Banner to include a picture of happy teen playing sports or out in park without glasses. To portray the new ability to see without glasses.
ORTHO-K #1 MYOPIA control treatment for children
- Corrects your vision while you sleep
- Creates crisp clear vision all day
- Freedom: No glasses, No Surgery, No soft lenses
-Safe and effective for children and adults

Target Market(s)

8-25 years old

Industry/Entity Type

Health Care

Font styles to use
Sans Serif

Colors
0692cd
cee9f5
ecf7fb
ffffff
86cfc6

Requirements
Must have
• Picture of teen playing sports or outdoors without glasses
Nice to have
• office logo on banner. happy color blue, green, white.
• Modern font: century gothic

```html
<!DOCTYPE html>
<html lang="en">
<head>
<meta charset="utf-8">
<title>Ortho-K Myopia Control Treatment for Children</title>
<link rel="stylesheet" href="https://fonts.googleapis.com/css2?family=Comic+Neue:wght@400;700&family=Roboto:wght@300;500&display=swap">
<style>
  :root {
    --stage: #e6e8e8;
    --paper: #ffffff;
    --haze: #eef5fb;
    --sky-top: #cfe2f3;
    --sky: #9cc6ea;
    --sky-deep: #4f93d3;
    --sun: #f4f9fd;
    --grass: #b9c99a;
    --headline: #5d5d5f;
    --band: #656567;
    --accent: #f7cf3c;
    --accent-text: #5d5d5f;
    --bullet: #ffffff;
    --brand: #6a6a6c;
  }
  * { margin: 0; padding: 0; box-sizing: border-box; }
  html, body { width: 960px; height: 1200px; overflow: hidden; background: var(--stage); }
  .poster {
    position: absolute; left: 130px; top: 30px;
    width: 700px; height: 1140px;
    background: var(--paper);
    overflow: hidden;
  }
  .poster-header {
    position: absolute; left: 0; top: 0; width: 100%; height: 400px;
    background: linear-gradient(180deg, var(--paper) 0%, var(--paper) 60%, var(--haze) 100%);
  }
  .brand {
    position: absolute; left: 80px; top: 110px;
    display: flex; flex-direction: column; align-items: flex-start;
    font-family: "Roboto", sans-serif; font-weight: 300;
    color: var(--brand); letter-spacing: 1px; line-height: 1.15;
  }
  .brand-mark { width: 46px; height: 46px; background: var(--accent); margin-bottom: 16px; }
  .brand-name { font-size: 22px; }
  .brand-sub { font-size: 18px; }
  .headline {
    position: absolute; left: 298px; top: 100px;
    font-family: "Comic Neue", sans-serif; font-weight: 700;
    font-size: 44px; line-height: 1.25; letter-spacing: 1px;
    color: var(--headline); text-transform: uppercase;
  }
  .hero-photo {
    position: absolute; left: 0; top: 400px; width: 100%; height: 430px;
    background:
      radial-gradient(ellipse 220px 180px at 70% 35%, var(--sun) 0%, rgba(244,249,253,0) 100%),
      linear-gradient(180deg, var(--sky-top) 0%, var(--sky) 40%, var(--sky-deep) 82%, var(--grass) 100%);
  }
  .benefits {
    position: absolute; left: 0; top: 830px; width: 100%; height: 225px;
    background: var(--band);
  }
  .benefit-list {
    list-style: none; position: absolute; left: 0; top: 22px; width: 100%;
    text-align: center;
    font-family: "Comic Neue", sans-serif; font-weight: 700;
    font-size: 23px; color: var(--bullet);
  }
  .benefit-list li { height: 48px; line-height: 36px; }
  .benefit-rules { position: absolute; left: 0; top: 0; }
  .contact-bar {
    position: absolute; left: 0; top: 1055px; width: 100%; height: 85px;
    background: var(--accent);
    display: flex; align-items: center; justify-content: center; gap: 16px;
    font-family: "Roboto", sans-serif; font-weight: 500; color: var(--accent-text);
  }
  .contact-phone { font-size: 28px; display: flex; align-items: center; gap: 8px; }
  .contact-web { font-size: 22px; display: flex; align-items: center; gap: 6px; }
</style>
</head>
<body>
  <main class="poster">
    <header class="poster-header">
      <div class="brand">
        <span class="brand-mark"></span>
        <span class="brand-name">TARNOBELLE</span>
        <span class="brand-sub">OPTOMETRY</span>
      </div>
      <h1 class="headline">Ortho-K#1<br>Myopia<br>Control<br>Treatment<br>For Children</h1>
    </header>

    <div class="hero-photo" role="img" aria-label="Photo of a group of happy children in colourful t-shirts jumping in the air outdoors under a bright blue sky"></div>

    <section class="benefits">
      <svg class="benefit-rules" width="700" height="225" viewBox="0 0 700 225" aria-hidden="true">
        <g fill="none" stroke="var(--accent)" stroke-width="1.5" stroke-linecap="round">
          <path d="M190 66 Q270 58 350 64 T520 60"/>
          <path d="M200 114 Q280 106 360 112 T510 108"/>
          <path d="M120 162 Q240 152 360 160 T590 156"/>
        </g>
      </svg>
      <ul class="benefit-list">
        <li>Corrects your vision while you sleep</li>
        <li>Creates crisp clear vision all day</li>
        <li>Freedom: No glasses, No Surgery, No soft lenses</li>
        <li>Safe and effective for children and adults "</li>
      </ul>
    </section>

    <footer class="contact-bar">
      <span class="contact-phone">
        <svg width="16" height="16" viewBox="0 0 16 16" aria-hidden="true">
          <circle cx="8" cy="8" r="8" fill="var(--paper)"/>
          <path d="M5 4.5 l1.6 -0.3 l0.8 2 l-1 0.8 q0.8 1.7 2.5 2.6 l0.8 -1 l2 0.8 l-0.3 1.6 q-4.8 0.2 -6.4 -6.5z" fill="var(--accent)"/>
        </svg>
        818-555-0147
      </span>
      <span class="contact-web">
        <svg width="12" height="12" viewBox="0 0 12 12" aria-hidden="true">
          <circle cx="6" cy="6" r="5" fill="none" stroke="var(--paper)" stroke-width="1.2"/>
          <path d="M1 6h10M6 1q-3 5 0 10M6 1q3 5 0 10" fill="none" stroke="var(--paper)" stroke-width="1"/>
        </svg>
        www.tarnobelle.com
      </span>
    </footer>
  </main>
</body>
</html>
```